Landscaping company needs bold flyer

We are a new landscaping company that requires a flyer to advertise our business. It should be bold and reflect our creative outlook. Our services include paving, driveways, fencing, brickwork, planting and turfing and artificial grass. We pride ourself on quality workmanship at an affordable price. Here is the link to our website http://www.fernhollow-gardens.com/

Industry/Entity Type

Landscaping

Font styles to use
Sans Serif

Colors
000000
9bcb3c

Requirements
Nice to have
• I'd like a design without any photographs on it. My brother has had some leaflets designed which I like,I'd like something similar. I've uploaded pictures of them.
Should not have
• The designs that have been submitted thus far have all been very simlilar. Could someone please try to create an original design, maybe with out any pictures on it. Please do not copy directly from my website, the link is purely for information

```html
<!DOCTYPE html>
<html lang="en">
<head>
<meta charset="utf-8">
<title>Fernhollow Gardens – Flyer</title>
<link href="https://fonts.googleapis.com/css2?family=Lato:wght@400;700;900&display=swap" rel="stylesheet">
<style>
  :root {
    --black: #000000;
    --ink: #111111;
    --green: #9bcb3c;
    --green-deep: #5f9a2c;
    --text: #2b2b2b;
    --white: #ffffff;
    --stage: #e4e4e4;
    --paving-light: #e9eaec;
    --paving-mid: #cfd1d4;
  }
  * { margin: 0; padding: 0; box-sizing: border-box; }
  html, body { width: 1075px; height: 1200px; overflow: hidden; }
  body { background: var(--stage); font-family: "Lato", sans-serif; position: relative; }

  .flyer {
    position: absolute; left: 113px; top: 0;
    width: 848px; height: 1200px; overflow: hidden;
    background: var(--paving-light);
  }

  .paving-backdrop {
    position: absolute; left: 0; top: 230px; width: 100%; height: 770px;
    background: linear-gradient(to bottom, var(--paving-mid) 0%, var(--paving-light) 60%, #f2f2f3 100%);
  }

  .header {
    position: absolute; left: 0; top: 0; width: 100%; height: 330px;
    background: linear-gradient(to bottom, var(--ink) 0%, #1a1a1a 62%, rgba(26,26,26,0) 100%);
  }
  .brand {
    position: absolute; top: 34px; left: 0; width: 100%;
    display: flex; flex-direction: column; align-items: center;
    color: var(--white); font-weight: 900; line-height: 1;
  }
  .brand-name { font-size: 66px; letter-spacing: 0; }
  .brand-sub {
    align-self: flex-end; margin-right: 218px; margin-top: 10px;
    font-size: 27px; letter-spacing: 1.5px;
  }

  .project-photo {
    position: absolute; border: 9px solid var(--white);
    box-shadow: 0 6px 14px rgba(0,0,0,0.35);
  }
  .project-photo--left {
    left: 50px; top: 190px; width: 290px; height: 230px; transform: rotate(8deg);
    background: #6fa33a;
  }
  .project-photo--right {
    left: 520px; top: 190px; width: 296px; height: 270px; transform: rotate(-8deg);
    background: #649a34;
  }
  .project-photo--center {
    left: 297px; top: 251px; width: 264px; height: 262px;
    background: #7b9a52;
  }

  .section-tab {
    position: absolute; left: 0; height: 50px; padding-left: 22px;
    background: var(--black); color: var(--green);
    font-weight: 900; font-size: 34px; line-height: 50px; letter-spacing: 0.5px;
    clip-path: polygon(0 0, 100% 0, calc(100% - 22px) 100%, 0 100%);
  }
  .section-tab--about { top: 537px; width: 312px; }
  .section-tab--service { top: 746px; width: 357px; }

  .about-copy {
    position: absolute; left: 23px; top: 602px; width: 805px;
    color: var(--text); font-size: 15.5px; line-height: 1.3; text-align: justify;
  }
  .about-copy p + p { margin-top: 8px; }

  .service-list {
    position: absolute; left: 23px; top: 818px; width: 800px;
    list-style: none; display: grid; grid-template-columns: 424px 1fr; row-gap: 10px;
  }
  .service-item {
    display: flex; align-items: center; gap: 12px;
    color: var(--text); font-size: 28px; letter-spacing: 1.4px; text-transform: uppercase; height: 32px;
  }
  .service-icon { width: 20px; height: 20px; flex: none; }

  .lawn-strip {
    position: absolute; left: 0; top: 965px; width: 100%; height: 113px;
    background: linear-gradient(to bottom, rgba(155,203,60,0) 0%, var(--green) 35%, var(--green-deep) 100%);
  }

  .footer {
    position: absolute; left: 0; top: 1076px; width: 100%; height: 124px;
    background: var(--black);
  }
  .contact-list {
    position: absolute; left: 99px; top: 28px; list-style: none;
    color: var(--white); font-weight: 700; font-size: 19px;
  }
  .contact-list li { display: flex; align-items: center; gap: 9px; height: 24px; }
  .contact-icon { width: 15px; height: 15px; }
  .footer-brand {
    position: absolute; right: 100px; top: 30px;
    display: flex; flex-direction: column; align-items: flex-end;
    color: var(--white); font-weight: 900; line-height: 1;
  }
  .footer-brand-name { font-size: 34px; }
  .footer-brand-sub { font-size: 14px; letter-spacing: 1px; margin-top: 5px; }
</style>
</head>
<body>
<main class="flyer">
  <div class="paving-backdrop" role="img" aria-label="Grey stone paving backdrop"></div>

  <header class="header">
    <h1 class="brand">
      <span class="brand-name">FERNHOLLOW</span>
      <span class="brand-sub">GARDENS</span>
    </h1>
  </header>

  <div class="project-photo project-photo--left" role="img" aria-label="Project photo: paved path beside a lawn"></div>
  <div class="project-photo project-photo--right" role="img" aria-label="Project photo: curved stone path through a landscaped garden"></div>
  <div class="project-photo project-photo--center" role="img" aria-label="Project photo: new timber fence and lawn"></div>

  <h2 class="section-tab section-tab--about">ABOUT US</h2>
  <div class="about-copy">
    <p>We at Fernhollow Gardens are a professional, experienced landscaping business that delivers premium garden construction at an affordable price. We provide all aspects of hard and soft landscaping throughout Surrey and surrounding areas.</p>
    <p>We pride ourselves on excellent workmanship and attention to detail. Using only top quality materials to ensure an outstanding and long-lasting finish, installed using both traditional and modern techniques.</p>
  </div>

  <h2 class="section-tab section-tab--service">OUR SERVICE</h2>
  <ul class="service-list">
    <li class="service-item"><svg class="service-icon" viewBox="0 0 20 20"><rect width="20" height="20" rx="4" fill="#9bcb3c"/><circle cx="10" cy="10" r="5" fill="#111"/></svg>Driveways</li>
    <li class="service-item"><svg class="service-icon" viewBox="0 0 20 20"><rect width="20" height="20" rx="4" fill="#9bcb3c"/><path d="M10 4 L15 10 L5 10 Z M8 10 h4 v5 h-4 Z" fill="#111"/></svg>Planting &amp; Turfing</li>
    <li class="service-item"><svg class="service-icon" viewBox="0 0 20 20"><rect width="20" height="20" rx="4" fill="#9bcb3c"/><path d="M10 4 L15 9 H12 V16 H8 V9 H5 Z" fill="#111"/></svg>Garden Design</li>
    <li class="service-item"><svg class="service-icon" viewBox="0 0 20 20"><rect width="20" height="20" rx="4" fill="#9bcb3c"/><path d="M5 5 h3 v10 h-3 Z M9 5 h3 v10 h-3 Z M13 5 h2 v10 h-2 Z" fill="#111"/></svg>Fencing &amp; Decking</li>
    <li class="service-item"><svg class="service-icon" viewBox="0 0 20 20"><rect width="20" height="20" rx="4" fill="#9bcb3c"/><rect x="5" y="5" width="10" height="10" rx="1.5" fill="#111"/></svg>Paving &amp; Brickwork</li>
    <li class="service-item"><svg class="service-icon" viewBox="0 0 20 20"><rect width="20" height="20" rx="4" fill="#9bcb3c"/><path d="M5 15 L7 7 L9 15 L11 5 L13 15 L15 8 L15 15 Z" fill="#111"/></svg>Artificial Grass</li>
  </ul>

  <div class="lawn-strip" role="img" aria-label="Band of green grass"></div>

  <footer class="footer">
    <ul class="contact-list">
      <li><svg class="contact-icon" viewBox="0 0 16 16"><circle cx="8" cy="8" r="7" fill="none" stroke="#fff" stroke-width="1.4"/><path d="M5.5 4.5 l1.5 0 l0.6 1.8 l-1 0.8 a5 5 0 0 0 2.3 2.3 l0.8 -1 l1.8 0.6 l0 1.5 a1 1 0 0 1 -1 0.8 a6 6 0 0 1 -5.8 -5.8 a1 1 0 0 1 0.8 -1 Z" fill="#fff"/></svg>07700 900 482</li>
      <li><svg class="contact-icon" viewBox="0 0 16 16"><circle cx="8" cy="8" r="7" fill="none" stroke="#fff" stroke-width="1.4"/><rect x="4" y="5" width="8" height="6" fill="none" stroke="#fff" stroke-width="1.2"/><path d="M4 5 L8 8.5 L12 5" fill="none" stroke="#fff" stroke-width="1.2"/></svg>info@fernhollow-gardens.com</li>
      <li><svg class="contact-icon" viewBox="0 0 16 16"><circle cx="8" cy="8" r="7" fill="none" stroke="#fff" stroke-width="1.4"/><ellipse cx="8" cy="8" rx="3" ry="7" fill="none" stroke="#fff" stroke-width="1.1"/><path d="M1 8 H15" stroke="#fff" stroke-width="1.1"/></svg>fernhollow-gardens.com</li>
    </ul>
    <div class="footer-brand">
      <span class="footer-brand-name">FERNHOLLOW</span>
      <span class="footer-brand-sub">GARDENS</span>
    </div>
  </footer>
</main>
</body>
</html>
```